Save our Business Card - We need your help

We need a fresh look on our business cards. We like it as it is, but it's not quite getting the 'wow' effect that we desire.
We're a tech startup building a cloud based solution for retailers consisting of Point of Sale, Inventory management and CRM.
The design should communicate a sense of a company that cares about the little things, design and relationships.
You can have a look at our website www.tillnest.com to get a feel for what we're like. Please feel free to message us for any further clarification
Target Market(s)
Our Customers are retail busines owners, cafe owners, other startups etc.
Industry/Entity Type
Building
Colors
Designer to choose colors to be used in the design.
Look and feel
Each slider illustrates characteristics of the customer's brand and the style your logo design should communicate.

```html
<!DOCTYPE html>
<html lang="en">
<head>
<meta charset="utf-8">
<title>TillNest Business Card</title>
<link href="https://fonts.googleapis.com/css2?family=Michroma&family=Ubuntu:wght@400;500&display=swap" rel="stylesheet">
<style>
  :root {
    --orange: #ee9a22;
    --orange-deep: #e0651e;
    --grey-light: #f2f2f2;
    --grey-mid: #c9c8c6;
    --grey-text: #5f5f5f;
    --white: #ffffff;
    --page: #ffffff;
  }
  * { box-sizing: border-box; margin: 0; padding: 0; }
  html, body { width: 1200px; height: 600px; overflow: hidden; background: var(--page); }
  .canvas {
    position: relative;
    width: 1200px;
    height: 600px;
    font-family: "Ubuntu", sans-serif;
  }
  .card {
    position: absolute;
    top: 140px;
    width: 530px;
    height: 320px;
    border-radius: 16px;
    overflow: hidden;
  }

  /* Front card */
  .card-front { left: 45px; background: var(--orange); }
  .front-top {
    position: absolute; left: 0; top: 0; width: 100%; height: 142px;
    background: radial-gradient(ellipse at 60% 30%, var(--white) 0%, var(--grey-light) 25%, var(--grey-mid) 80%);
  }
  .front-divider {
    position: absolute; left: 0; top: 150px; width: 100%; height: 4px;
    background: var(--white);
  }
  .brand {
    position: absolute; display: flex; align-items: center;
  }
  .brand-mark { background: var(--orange); border-radius: 3px; }
  .brand-name { color: var(--orange); font-weight: 500; letter-spacing: 0.5px; }
  .card-front .brand { left: 30px; top: 62px; gap: 12px; }
  .card-front .brand-mark { width: 32px; height: 32px; }
  .card-front .brand-name { font-size: 28px; }

  .holder { position: absolute; left: 22px; top: 172px; }
  .holder-name {
    font-family: "Michroma", sans-serif;
    color: var(--white);
    font-size: 24px;
    letter-spacing: 1px;
    line-height: 1.1;
  }
  .holder-title {
    font-family: "Michroma", sans-serif;
    color: var(--orange-deep);
    font-size: 12px;
    letter-spacing: 2px;
    margin-top: 2px;
  }
  .contacts {
    position: absolute; left: 22px; top: 232px;
    display: grid;
    grid-template-columns: 124px 150px;
    row-gap: 4px;
    column-gap: 0;
    color: var(--white);
    font-size: 14px;
  }
  .contact { display: flex; align-items: center; gap: 8px; white-space: nowrap; }
  .contact svg { width: 14px; height: 14px; flex: none; fill: var(--orange-deep); }

  /* Back card */
  .card-back { left: 625px; background: var(--orange); }
  .back-panel { position: absolute; inset: 0; }
  .card-back .brand {
    left: 0; right: 0; top: 128px; justify-content: center; gap: 18px;
  }
  .card-back .brand-mark { width: 62px; height: 62px; }
  .card-back .brand-name { font-size: 52px; }
</style>
</head>
<body>
<main class="canvas">

  <section class="card card-front" aria-label="Business card front">
    <div class="front-top"></div>
    <div class="front-divider"></div>

    <div class="brand">
      <span class="brand-mark"></span>
      <span class="brand-name">TillNest</span>
    </div>

    <div class="holder">
      <h1 class="holder-name">YOUR NAME</h1>
      <p class="holder-title">JOB TITLE</p>
    </div>

    <ul class="contacts" style="list-style:none">
      <li class="contact">
        <svg viewBox="0 0 14 14" aria-hidden="true"><path d="M4 0h6a1 1 0 0 1 1 1v12a1 1 0 0 1-1 1H4a1 1 0 0 1-1-1V1a1 1 0 0 1 1-1zm0 2v9h6V2zm3 9.6a.8.8 0 1 0 0 1.6.8.8 0 0 0 0-1.6z"/></svg>
        Mobile number
      </li>
      <li class="contact">
        <svg viewBox="0 0 14 14" aria-hidden="true"><path d="M1 4c0-2 3-3 6-3s6 1 6 3v1.5h-3.5V4h-5v1.5H1zM3.5 6h7L13 10v3H1v-3zm3.5 1.5a2 2 0 1 0 0 4 2 2 0 0 0 0-4z"/></svg>
        office number
      </li>
      <li class="contact">
        <svg viewBox="0 0 14 14" aria-hidden="true"><path d="M0 3h14v8H0zm1.2 1L7 8l5.8-4z"/></svg>
        email address
      </li>
      <li class="contact">
        <svg viewBox="0 0 14 14" aria-hidden="true"><path d="M7 0a7 7 0 1 0 0 14A7 7 0 0 0 7 0zm0 1.3c.9 0 1.8 1.6 2.1 4.2H4.9C5.2 2.9 6.1 1.3 7 1.3zM1.4 5.5h2.3a16 16 0 0 0 0 3H1.4a5.8 5.8 0 0 1 0-3zm8.9 0h2.3a5.8 5.8 0 0 1 0 3h-2.3a16 16 0 0 0 0-3zM4.9 8.5h4.2c-.3 2.6-1.2 4.2-2.1 4.2s-1.8-1.6-2.1-4.2z"/></svg>
        www.tillnest.com
      </li>
      <li class="contact">
        <svg viewBox="0 0 14 14" aria-hidden="true"><path d="M7 0a4.6 4.6 0 0 1 4.6 4.6C11.6 8 7 14 7 14S2.4 8 2.4 4.6A4.6 4.6 0 0 1 7 0zm0 2.8a1.8 1.8 0 1 0 0 3.6 1.8 1.8 0 0 0 0-3.6z"/></svg>
        Address
      </li>
    </ul>
  </section>

  <section class="card card-back" aria-label="Business card back">
    <svg class="back-panel" viewBox="0 0 530 320" aria-hidden="true">
      <defs>
        <radialGradient id="backShade" cx="50%" cy="45%" r="65%">
          <stop offset="0%" stop-color="#ffffff"/>
          <stop offset="45%" stop-color="#ececec"/>
          <stop offset="100%" stop-color="#cfcecc"/>
        </radialGradient>
      </defs>
      <path d="M0 16 Q0 0 16 0 H440 Q500 0 505 18 L512 60 V300 Q512 306 506 306 H90 Q30 306 20 290 L0 250 Z" fill="url(#backShade)"/>
    </svg>
    <div class="brand">
      <span class="brand-mark"></span>
      <span class="brand-name">TillNest</span>
    </div>
  </section>

</main>
</body>
</html>
```